Bref créative
Stationary for Visual Explanation Business
Bus Card, Stationary
Professional
Martin Pelloway
CEO & Founder
487 E 29th Street, Suite 4B
New York, NY 10027
USA
martin@lumbrivista.com
www.lumbrivista.com
Looking for clean and modern sophisticated look and feel for a marketing service business company that offers visual explanations for technology companies. Not cutesy. A blend of QXR combined with creative agency.
The letterhead will serve as my proposal template. I will use it for placing text and illustrations.
I want to keep with the orange and gray of the logo.
I wil supply the AI version of the logo shortly.
Logo AI File with tagline and name
Logo Ai File with company name and no tagline
Logo Ai file with no tagline and no company name

```html
<!DOCTYPE html>
<html lang="en">
<head>
<meta charset="utf-8">
<title>Lumbri Vista — Business Cards</title>
<link rel="stylesheet" href="https://fonts.googleapis.com/css2?family=Open+Sans:wght@400;600;700&display=swap">
<style>
  :root {
    --stage: #e9e6e2;
    --card: #ffffff;
    --orange: #f39a1e;
    --gray: #5d666d;
    --gray-light: #9aa2a8;
    --edge: #c7ccd0;
  }
  html, body {
    margin: 0;
    width: 1200px;
    height: 655px;
    overflow: hidden;
    background: var(--stage);
    font-family: "Open Sans", Arial, sans-serif;
  }
  .stage {
    position: relative;
    width: 1200px;
    height: 655px;
  }
  .card {
    position: absolute;
    top: 185px;
    width: 500px;
    height: 286px;
    background: var(--card);
    border-radius: 16px;
    box-shadow: 0 6px 18px rgba(0,0,0,0.18);
    overflow: hidden;
  }
  .card--front { left: 70px; }
  .card--back { left: 630px; }
  .card__tab {
    position: absolute;
    left: 0;
    bottom: 22px;
    width: 7px;
    height: 64px;
    background: var(--edge);
  }
  .brand {
    position: absolute;
    display: flex;
    flex-direction: column;
  }
  .brand__row {
    display: flex;
    align-items: center;
    gap: 10px;
  }
  .brand__square {
    width: 30px;
    height: 30px;
    background: var(--orange);
  }
  .brand__name {
    font-size: 34px;
    font-weight: 600;
    color: var(--gray);
    letter-spacing: -0.5px;
    line-height: 1;
  }
  .brand__tagline {
    margin-top: 5px;
    margin-left: 40px;
    font-size: 7.5px;
    font-weight: 600;
    letter-spacing: 1px;
    color: var(--gray-light);
    text-transform: uppercase;
  }
  .card--front .brand { left: 34px; top: 48px; }
  .card--back .brand { right: 26px; top: 122px; }
  .card--back .brand__name { font-size: 30px; }
  .card--back .brand__square { width: 26px; height: 26px; }
  .card--back .brand__tagline { margin-left: 36px; font-size: 6.5px; }
  .person {
    position: absolute;
  }
  .person__name {
    font-size: 14px;
    font-weight: 600;
    color: var(--orange);
    margin: 0;
  }
  .person__role {
    font-size: 9.5px;
    color: var(--gray);
    margin: 3px 0 0;
  }
  .card--front .person { left: 305px; top: 128px; }
  .card--back .person { left: 34px; top: 56px; }
  .contact {
    position: absolute;
    left: 34px;
    bottom: 26px;
    font-size: 8.5px;
    line-height: 1.45;
    color: var(--gray);
    font-style: normal;
  }
  .contact__web {
    font-weight: 700;
  }
</style>
</head>
<body>
<main class="stage">
  <section class="card card--front">
    <span class="card__tab"></span>
    <div class="brand">
      <div class="brand__row">
        <span class="brand__square"></span>
        <span class="brand__name">Lumbri Vista</span>
      </div>
      <span class="brand__tagline">Visual explanations for tech brands</span>
    </div>
    <div class="person">
      <p class="person__name">Martin Pelloway</p>
      <p class="person__role">CEO &amp; Founder</p>
    </div>
    <address class="contact">
      487 E 29th Street, Suite 4B<br>
      New York, NY 10027<br>
      USA<br>
      P: (917) 555-0148<br>
      E: martin@lumbrivista.com<br>
      <span class="contact__web">www.lumbrivista.com</span>
    </address>
  </section>

  <section class="card card--back">
    <span class="card__tab"></span>
    <div class="person">
      <p class="person__name">Martin Pelloway</p>
      <p class="person__role">CEO &amp; Founder</p>
    </div>
    <div class="brand">
      <div class="brand__row">
        <span class="brand__square"></span>
        <span class="brand__name">Lumbri Vista</span>
      </div>
      <span class="brand__tagline">Visual explanations for tech brands</span>
    </div>
    <address class="contact">
      487 E 29th Street, Suite 4B<br>
      New York, NY 10027<br>
      USA<br>
      P: (917) 555-0148<br>
      E: martin@lumbrivista.com<br>
      <span class="contact__web">www.lumbrivista.com</span>
    </address>
  </section>
</main>
</body>
</html>
```